I need a graphic for that looks like a fancy spread sheet for a predictions game for a reality show. I want there to be 3 columns, 1:Player A, 2: Question, 3: Player B. There should be at least 10 rows. I am looking for a photoshop template that I can customize later. I have attached the graphic needed for the name of the shows as well as a very basic version of what I am looking for. Please let me know if you need additional information. It should be themed with roses and wedding rings.
SIZE:
1080px by 1920px

Font styles to use
Decorative

Colors
ec1f27
9bcb3c

Requirements
Must have
• The logo for Plovex and Velmora. 1080px by 1920px in size.
Nice to have
• Would be nice to have rose vines as the dividers

```html
<!DOCTYPE html>
<html lang="en">
<head>
<meta charset="utf-8">
<title>Prediction Game Sheet</title>
<link href="https://fonts.googleapis.com/css2?family=Kaushan+Script&family=Roboto:wght@700;900&display=swap" rel="stylesheet">
<style>
  :root {
    --green: #9bcb3c;
    --red: #ec1f27;
    --white: #ffffff;
    --brand-red: #c8202f;
    --navy: #1c2a4a;
  }
  * { box-sizing: border-box; margin: 0; padding: 0; }
  html, body { width: 675px; height: 1200px; overflow: hidden; }
  body { font-family: "Roboto", Arial, sans-serif; background: var(--white); }
  .sheet {
    position: relative; width: 675px; height: 1200px;
    background: linear-gradient(to right, var(--green) 0 336px, var(--red) 336px 675px);
  }
  .masthead {
    position: absolute; left: 0; top: 0; width: 675px; height: 164px;
    background: var(--white);
  }
  .brand {
    position: absolute; display: flex; align-items: center; gap: 8px;
    font-family: "Roboto", Arial, sans-serif; font-weight: 900;
  }
  .brand--show { left: 38px; top: 62px; font-size: 34px; color: var(--brand-red); letter-spacing: -0.5px; }
  .brand--show .dot { width: 14px; height: 14px; border-radius: 50%; background: var(--brand-red); }
  .brand--game {
    right: 38px; top: 66px; font-size: 15px; color: var(--navy);
    flex-direction: column; gap: 4px; text-transform: uppercase; line-height: 1; text-align: center;
  }
  .brand--game .square { width: 30px; height: 30px; background: var(--navy); }

  .heading { position: absolute; color: var(--white); text-align: center; }
  .heading .player { display: block; font-weight: 700; font-size: 21px; letter-spacing: 0.5px; line-height: 1; }
  .heading .script { display: block; font-family: "Kaushan Script", cursive; font-size: 36px; line-height: 1.1; margin-top: 10px; }
  .heading--a { left: 28px; width: 200px; top: 193px; }
  .heading--b { left: 448px; width: 200px; top: 193px; }
  .heading--q { left: 238px; width: 200px; top: 204px; }
  .heading--q .script { margin-top: 0; }

  .column {
    position: absolute; top: 314px; height: 812px; width: 185px;
    border: 4px solid var(--white);
    display: flex; flex-direction: column;
  }
  .column--a { left: 36px; }
  .column--q { left: 244px; }
  .column--b { left: 455px; }
  .cell {
    position: relative; flex: 1;
    border-top: 2px solid var(--white);
    color: var(--white);
  }
  .cell:first-child { border-top: 0; }
  .cell .prompt {
    display: block; margin: 4px auto 0; width: 134px;
    font-weight: 700; font-size: 11.3px; line-height: 14px; text-align: center;
  }
  .cell .num {
    position: absolute; right: 7px; bottom: 1px;
    font-family: "Kaushan Script", cursive; font-size: 13px;
  }
</style>
</head>
<body>
<main class="sheet">
  <header class="masthead">
    <div class="brand brand--show"><span>Velmora</span><span class="dot"></span></div>
    <div class="brand brand--game"><span class="square"></span><span>Plovex</span><span>Challenge</span></div>
  </header>

  <div class="heading heading--a"><span class="player">TIM A</span><span class="script">Answer</span></div>
  <div class="heading heading--q"><span class="script">Questions</span></div>
  <div class="heading heading--b"><span class="player">TIM B</span><span class="script">Answer</span></div>

  <section class="column column--a">
    <div class="cell"><span class="prompt">Lorem ipsum dolor sit amet, consectetur adipiscing elit. In ante ipsum, dictum sit amet sem eget, mollis</span></div>
    <div class="cell"></div><div class="cell"></div><div class="cell"></div><div class="cell"></div>
    <div class="cell"></div><div class="cell"></div><div class="cell"></div><div class="cell"></div><div class="cell"></div>
  </section>

  <section class="column column--q">
    <div class="cell"><span class="prompt">Lorem ipsum dolor sit amet, consectetur adipiscing elit. In ante ipsum, dictum sit amet sem eget, mollis</span><span class="num">1</span></div>
    <div class="cell"><span class="num">2</span></div>
    <div class="cell"><span class="num">3</span></div>
    <div class="cell"><span class="num">4</span></div>
    <div class="cell"><span class="num">5</span></div>
    <div class="cell"><span class="num">6</span></div>
    <div class="cell"><span class="num">7</span></div>
    <div class="cell"><span class="num">8</span></div>
    <div class="cell"><span class="num">9</span></div>
    <div class="cell"><span class="num">10</span></div>
  </section>

  <section class="column column--b">
    <div class="cell"><span class="prompt">Lorem ipsum dolor sit amet, consectetur adipiscing elit. In ante ipsum, dictum sit amet sem eget, mollis</span></div>
    <div class="cell"></div><div class="cell"></div><div class="cell"></div><div class="cell"></div>
    <div class="cell"></div><div class="cell"></div><div class="cell"></div><div class="cell"></div><div class="cell"></div>
  </section>
</main>
</body>
</html>
```